High quality childcare centre needs a roadside banner

We need a banner designed that advertises our achievement of being rated Exceeding Civic Nurture Benchmark. Which is the highest rating you can be award as part of the assessment and rating process.

Attached pdf is purely an example although the text as it stands needs to be incorporated.

Please see below for the corporate colors:

Magenta
C-0 M-100 Y-33 K-10
bf00bf

Green
C-78 M-0 Y-100 K-0
00bf00

Target Market(s)

Parents of young children that need childcare

Industry/Entity Type

Childcare

Font styles to use
Sans Serif

Requirements
Must have
• As it is a roadside banner the text should be big, bold and easy to read therefore do not use serif fonts
• Please change found to find
• Logo - see attached
• Supplied wording - see attached
• The specs for the banner are 4m x 1.25m or 4000mm x 1250mm
• The files need to be in the following format:
• jpg, eps and ai.
• Bleeds if relevant
Nice to have
• Other marketing road signs incorporate the attached 'grobold' font
• We also have a motto - 'out of little things, big things grow'
Should not have
• Serif fonts

```html
<!DOCTYPE html>
<html lang="en">
<head>
<meta charset="utf-8">
<title>Bright Sprouts – Roadside Banner</title>
<link rel="stylesheet" href="https://fonts.googleapis.com/css2?family=Fredoka:wght@600;700&family=Chewy&display=swap">
<style>
  :root {
    --magenta: #b82ad0;
    --green: #5cf01a;
    --green-band: #4cf20f;
    --white: #ffffff;
    --ink-shadow: rgba(60, 0, 70, 0.35);
  }
  * { box-sizing: border-box; margin: 0; padding: 0; }
  html, body {
    width: 1200px;
    height: 457px;
    overflow: hidden;
    background: var(--white);
  }
  .banner {
    position: relative;
    width: 1200px;
    height: 457px;
    background: var(--white);
    font-family: "Fredoka", "Arial Rounded MT Bold", sans-serif;
  }
  .top-stripe {
    position: absolute;
    left: 41px; top: 27px;
    width: 1118px; height: 28px;
    background: var(--green-band);
  }
  .motto-band {
    position: absolute;
    left: 41px; top: 346px;
    width: 1118px; height: 72px;
    background: var(--magenta);
  }
  .arc {
    position: absolute;
    left: 80px; top: 232px;
    width: 230px; height: 120px;
  }
  .brand {
    position: absolute;
    left: 66px; top: 62px;
    width: 200px;
    text-align: center;
    color: var(--magenta);
  }
  .brand-mark {
    display: block;
    width: 52px; height: 52px;
    margin: 0 auto 8px;
    border-radius: 50%;
    background: var(--magenta);
  }
  .brand-name {
    font-size: 27px;
    font-weight: 700;
    line-height: 1;
  }
  .brand-sub {
    margin-top: 6px;
    font-size: 9px;
    font-weight: 600;
    color: var(--green);
  }
  .headline {
    position: absolute;
    left: 310px; top: 112px;
    width: 580px;
    text-align: center;
  }
  .rated, .invite {
    color: var(--green);
    font-size: 30px;
    font-weight: 700;
    line-height: 1;
  }
  .rating {
    margin: 10px 0 8px;
    color: var(--magenta);
    font-size: 54px;
    font-weight: 700;
    line-height: 1.18;
    text-shadow: 2px 2px 0 var(--ink-shadow);
  }
  .motto {
    position: absolute;
    left: 300px; top: 352px;
    width: 560px;
    text-align: center;
    white-space: nowrap;
    color: var(--white);
    font-family: "Chewy", "Comic Sans MS", sans-serif;
    font-size: 40px;
    line-height: 1.45;
  }
  .photo { position: absolute; }
  .photo-child-blocks {
    left: 96px; top: 262px;
    width: 186px; height: 150px;
    border-radius: 10px;
    background: linear-gradient(135deg, #f6e2d6 0%, #f1c26a 45%, #7fd0f0 75%, #a7e06a 100%);
  }
  .photo-hands {
    left: 1050px; top: 62px;
    width: 109px; height: 210px;
    border-radius: 8px;
    background: linear-gradient(180deg, #f05aa0 0%, #f9d238 35%, #58c5e8 65%, #7cd65a 100%);
  }
  .photo-children {
    left: 834px; top: 282px;
    width: 318px; height: 84px;
    border-radius: 10px;
    background: linear-gradient(90deg, #f0b69a 0%, #e46fa4 30%, #7ac2ec 55%, #f3cd5a 75%, #e77fc6 100%);
  }
</style>
</head>
<body>
<main class="banner">
  <div class="top-stripe"></div>
  <div class="motto-band"></div>

  <svg class="arc" viewBox="0 0 230 120" aria-hidden="true">
    <path d="M 12 120 A 103 103 0 0 1 218 120" fill="none" stroke="var(--magenta)" stroke-width="14"/>
  </svg>

  <header class="brand">
    <span class="brand-mark"></span>
    <div class="brand-name">Bright Sprouts</div>
    <div class="brand-sub">Early Development &amp; Education Centre</div>
  </header>

  <section class="headline">
    <p class="rated">This service is rated</p>
    <h1 class="rating">‘Exceeding Civic<br>Nurture Benchmark’</h1>
    <p class="invite">Come in and find out why ......</p>
  </section>

  <p class="motto">'out of little things, big things grow'</p>

  <div class="photo photo-child-blocks" role="img" aria-label="Photo of a smiling toddler playing with colourful magnetic building tiles"></div>
  <div class="photo photo-hands" role="img" aria-label="Photo of children's hands painted in bright colours reaching upward"></div>
  <div class="photo photo-children" role="img" aria-label="Photo of a row of happy young children lying on their fronts"></div>
</main>
</body>
</html>
```